Kettle Lane Kitchen February contest

The website slider is 990 X 225 pixels to fit in with this website www.kettlelanekitchen.com.au
We would love a fun, lively, food-oriented slider created for Kettle Lane Kitchen website. Kettle Lane Kitchen is a central place where people who love food, cooking for their family and friends, and sharing recipes can hang out. We'd like the sliders to be simple, bright and to entice people to click on the link.
The banner ad needs to feature the Varnholt mixer, and to use a colour scheme that also works with the existing website. There's a blog with more information on the Varnholt mixer here http://kettlelanekitchen.com.au/uncategorized/upload-a-recipe-in-february-to-be-in-the-running-to-win-a-varnholt-mixer/
A slider in December was used to promote a similar competition which I will upload as inspiration, along with the image of the Varnholt mixer to use.
Main text: Add your best recipe by February 28 to win!
Smaller text: Best recipe as chosen by Kettle Lane Kitchen editors will win a Varnholt mixer worth $699.
Target Market(s)
Food lovers - home cooks and food bloggers. Mainly women, 30+
Industry/Entity Type
Chef

```html
<!DOCTYPE html>
<html lang="en">
<head>
<meta charset="utf-8">
<title>Kettle Lane Kitchen – February contest</title>
<link rel="stylesheet" href="https://fonts.googleapis.com/css2?family=Questrial&family=Open+Sans:wght@400;700&family=Permanent+Marker&display=swap">
<style>
  :root {
    --paper: #f1e8dc;
    --paper-dark: #e8dccb;
    --ink: #3e3833;
    --orange: #d9502a;
    --white: #ffffff;
    --mixer-teal: #3bb3c9;
    --photo-steel: #b9c2c4;
    --photo-warm: #e9d9c8;
  }
  * { box-sizing: border-box; margin: 0; padding: 0; }
  html, body { width: 1200px; height: 415px; overflow: hidden; }
  body {
    background: radial-gradient(ellipse at 40% 30%, var(--paper) 0%, var(--paper-dark) 100%);
    font-family: "Open Sans", Arial, sans-serif;
    color: var(--ink);
    position: relative;
  }
  .brand-badge {
    position: absolute; left: 57px; top: -18px;
    width: 192px; height: 192px; border-radius: 50%;
    background: var(--white);
    box-shadow: 0 0 0 3px var(--paper), 0 0 0 5px var(--paper-dark);
    display: flex; align-items: center; justify-content: center;
    z-index: 3;
  }
  .brand-badge .ring {
    width: 168px; height: 168px; border-radius: 50%;
    border: 3px solid var(--ink);
    display: flex; align-items: center; justify-content: center; text-align: center;
    padding-top: 14px;
  }
  .brand-name {
    font-family: "Questrial", sans-serif;
    font-size: 25px; line-height: 1.05; color: var(--ink);
  }
  .account-links {
    position: absolute; left: 1003px; top: 0; width: 123px; height: 30px;
    background: var(--white); border-radius: 0 0 4px 4px;
    display: flex; gap: 14px; justify-content: center; align-items: center;
    font-size: 13px;
  }
  .account-links a { color: var(--orange); text-decoration: none; }
  .tagline {
    position: absolute; left: 425px; top: 36px;
    font-family: "Questrial", sans-serif; font-size: 31px; letter-spacing: 0.5px;
    color: var(--ink);
  }
  .tagline-arrow { position: absolute; left: 862px; top: 40px; }
  .section-tabs {
    position: absolute; left: 257px; top: 108px; width: 330px; height: 44px;
    background: var(--white); border-radius: 4px 0 0 0;
    display: flex; align-items: center; gap: 22px; padding-left: 26px;
    font-size: 13px; font-weight: 700; color: var(--ink);
  }
  .section-tabs span { display: flex; align-items: center; gap: 5px; }
  .main-nav {
    position: absolute; left: 587px; top: 108px; width: 539px; height: 44px;
    background: var(--orange); border-radius: 0 5px 0 0;
    display: flex; align-items: center; justify-content: center;
    font-size: 13.5px; font-weight: 700; color: var(--white);
  }
  .main-nav .dot { margin: 0 9px; font-size: 10px; }
  .contest-banner {
    position: absolute; left: 57px; top: 152px; width: 1069px; height: 246px;
    background: linear-gradient(90deg, #f7f3ef 0%, var(--white) 30%);
    overflow: hidden;
  }
  .kitchen-photo {
    position: absolute; left: 646px; top: 0; width: 423px; height: 246px;
    background: linear-gradient(160deg, var(--photo-warm) 0%, var(--photo-steel) 45%, #d8dcd6 70%, #c98b62 100%);
  }
  .mixer-photo {
    position: absolute; left: 94px; top: 22px; width: 200px; height: 170px;
    border-radius: 40px 40px 10px 10px;
    background: linear-gradient(135deg, var(--mixer-teal) 0%, #cfd4d6 55%, #9aa3a6 100%);
  }
  .mixer-arrow { position: absolute; left: 300px; top: 130px; }
  .prize-disc {
    position: absolute; left: 370px; top: -36px; width: 300px; height: 300px;
    border-radius: 50%; background: var(--orange);
    color: var(--white); text-align: center; padding-top: 70px;
    font-family: "Questrial", sans-serif;
  }
  .prize-disc .line { font-size: 24px; letter-spacing: 0.5px; line-height: 1.3; }
  .prize-disc .line-strong { font-family: "Open Sans", sans-serif; font-weight: 700; font-size: 25px; letter-spacing: 1px; line-height: 1.3; }
  .prize-disc .call {
    font-family: "Permanent Marker", "Arial Black", sans-serif; font-size: 54px; line-height: 1.2; letter-spacing: 2px;
  }
  .prize-note {
    position: absolute; left: 32px; top: 200px; width: 340px;
    font-size: 13px; line-height: 1.4; color: var(--ink);
  }
  .prize-note strong { font-size: 16px; }
  .page-strip {
    position: absolute; left: 57px; top: 398px; width: 1069px; height: 17px; background: var(--white);
  }
</style>
</head>
<body>
  <div class="brand-badge"><div class="ring"><span class="brand-name">Kettle<br>Lane<br>Kitchen</span></div></div>

  <nav class="account-links"><a href="#">Register</a><a href="#">Login</a></nav>

  <p class="tagline">Join the community now!</p>
  <svg class="tagline-arrow" width="56" height="30" viewBox="0 0 56 30" aria-hidden="true">
    <path d="M2 24 Q24 30 48 8" fill="none" stroke="#d9502a" stroke-width="2"/>
    <path d="M38 8 L49 6 L47 17" fill="none" stroke="#d9502a" stroke-width="2"/>
  </svg>

  <nav class="section-tabs">
    <span><svg width="20" height="14" viewBox="0 0 20 14" aria-hidden="true"><path d="M1 4 H19 Q18 13 10 13 Q2 13 1 4Z" fill="#d9502a"/></svg>Recipes</span>
    <span><svg width="18" height="18" viewBox="0 0 18 18" aria-hidden="true"><circle cx="9" cy="7" r="6" fill="#d9502a"/><rect x="4" y="10" width="10" height="6" rx="1" fill="#d9502a"/></svg>Chefs</span>
    <span><svg width="20" height="18" viewBox="0 0 20 18" aria-hidden="true"><circle cx="10" cy="4" r="3.5" fill="#d9502a"/><circle cx="4" cy="8" r="3.5" fill="#d9502a"/><circle cx="16" cy="8" r="3.5" fill="#d9502a"/><circle cx="10" cy="13" r="4" fill="#d9502a"/></svg>Mentors</span>
  </nav>

  <nav class="main-nav">
    <span>Upload your recipe</span><span class="dot">●</span>
    <span>Prizes</span><span class="dot">●</span>
    <span>About</span><span class="dot">●</span>
    <span>FAQs</span><span class="dot">●</span>
    <span>Contact</span><span class="dot">●</span>
    <span>Blog</span>
  </nav>

  <section class="contest-banner">
    <div class="kitchen-photo" role="img" aria-label="Photo of chefs plating seafood salads in a busy kitchen"></div>
    <div class="mixer-photo" role="img" aria-label="Photo of the Varnholt stand mixer in teal with a steel bowl"></div>
    <svg class="mixer-arrow" width="50" height="24" viewBox="0 0 50 24" aria-hidden="true">
      <path d="M2 6 Q26 2 44 18" fill="none" stroke="#d9502a" stroke-width="2"/>
      <path d="M34 18 L45 19 L43 9" fill="none" stroke="#d9502a" stroke-width="2"/>
    </svg>
    <div class="prize-disc">
      <div class="line">ADD YOUR</div>
      <div class="line-strong">BEST RECIPE</div>
      <div class="line">BY FEBRUARY 28</div>
      <div class="call">TO WIN</div>
    </div>
    <p class="prize-note">*Best recipe as chosen by Kettle Lane Kitchen editors will win a Varnholt mixer worth <strong>$699.</strong></p>
  </section>
  <div class="page-strip"></div>
</body>
</html>
```